Gourmet butcher shop needs a business card design

We need a business card design for an upmarket butcher shop in Brisbane, Queensland Australia. We would prefer the card to be printed on a brown craft paper business card and would consider the use of raised print on the card. The card needs to make space for the usual information: ABN, address, telephone, facebook page. I stress it is a gourmet shop in a wealthy suburb. Thanks

Industry/Entity Type

Business

Contact Information for Business Card

Address Shop 7, Marrowbank Arcade, 417 Hollister Road, Wrenholme
Telephone 07 3581 4927
A.B.N. 53 874 910 326
Facebook www.facebook.com/quillbyprimecuts

Requirements
Should not have
• No need for a person's name or title

```html
<!DOCTYPE html>
<html lang="en">
<head>
<meta charset="utf-8">
<title>Quillby Prime Cuts — Business Card</title>
<link rel="stylesheet" href="https://fonts.googleapis.com/css2?family=Montserrat:wght@400;600;800&display=swap">
<style>
  :root {
    --backdrop: #e9e4de;
    --kraft: #c7ab8b;
    --kraft-edge: #b99c7b;
    --butcher-red: #b3202c;
    --ink: #2a2420;
  }
  * { box-sizing: border-box; margin: 0; padding: 0; }
  html, body {
    width: 1200px;
    height: 800px;
    overflow: hidden;
    background: var(--backdrop);
  }
  .canvas {
    position: relative;
    width: 1200px;
    height: 800px;
  }
  .business-card {
    position: absolute;
    left: 150px;
    top: 125px;
    width: 900px;
    height: 550px;
    background: var(--kraft);
    border: 1px solid var(--kraft-edge);
    font-family: "Montserrat", sans-serif;
    color: var(--ink);
  }
  .brand-name {
    position: absolute;
    left: 220px;
    top: 110px;
    font-weight: 800;
    font-size: 42px;
    line-height: 1.05;
    letter-spacing: 0.06em;
    text-transform: uppercase;
    color: var(--butcher-red);
  }
  .contact-details {
    position: absolute;
    left: 480px;
    top: 290px;
    font-weight: 400;
    font-size: 19px;
    line-height: 1.3;
    font-style: normal;
  }
  .contact-details .shop-number {
    color: var(--butcher-red);
    font-weight: 600;
  }
  .contact-details .phone { margin-top: 12px; font-size: 15px; }
  .contact-details .abn { font-size: 15px; }
  .contact-details .facebook {
    margin-top: 4px;
    font-size: 15px;
    font-weight: 600;
    letter-spacing: 0.03em;
    text-transform: uppercase;
    color: var(--butcher-red);
  }
</style>
</head>
<body>
  <main class="canvas">
    <section class="business-card" aria-label="Quillby Prime Cuts business card">
      <h1 class="brand-name">Quillby<br>Prime Cuts</h1>
      <address class="contact-details">
        <p class="shop-number">Shop 7</p>
        <p>Marrowbank Arcade</p>
        <p>417 Hollister Road</p>
        <p>Wrenholme</p>
        <p class="phone">07 3581 4927</p>
        <p class="abn">ABN 53 874 910 326</p>
        <p class="facebook">facebook.com/quillbyprimecuts</p>
      </address>
    </section>
  </main>
</body>
</html>
```